Business card design

I have a PDF of just what I want, but I need it to be digitized for Harlow Depot so I can edit and modify for new employees and reorder going forward

Business

```html
<!DOCTYPE html>
<html lang="en">
<head>
<meta charset="utf-8">
<title>Nova Property Managers – Business Card</title>
<link href="https://fonts.googleapis.com/css2?family=Roboto:wght@400;700&display=swap" rel="stylesheet">
<style>
  :root {
    --page-navy: #002340;
    --card-blue: #0a93d2;
    --card-edge: #d9ecf7;
    --band-black: #231f20;
    --text-white: #ffffff;
    --skyline-dark: #2a2a2a;
    --skyline-mid: #5a6f7c;
  }
  * { margin: 0; padding: 0; box-sizing: border-box; }
  html, body {
    width: 694px;
    height: 1200px;
    overflow: hidden;
    background: var(--page-navy);
    font-family: "Roboto", Arial, sans-serif;
  }
  .card {
    position: absolute;
    left: 86px;
    top: 164px;
    width: 550px;
    height: 880px;
    background: var(--card-blue);
    border: 1.5px solid var(--card-edge);
    border-radius: 36px;
    overflow: hidden;
    color: var(--text-white);
  }
  .brand-band {
    position: absolute;
    left: 0;
    top: 84px;
    width: 100%;
    height: 100px;
    background: var(--band-black);
    border-top: 3px solid var(--text-white);
    border-bottom: 3px solid var(--text-white);
    display: flex;
    align-items: center;
    justify-content: center;
  }
  .brand-name {
    font-weight: 700;
    font-size: 38px;
    letter-spacing: 1px;
    color: var(--text-white);
  }
  .contact {
    position: absolute;
    left: 0;
    top: 280px;
    width: 100%;
    text-align: center;
    font-weight: 400;
    letter-spacing: 0.4px;
  }
  .contact__name { font-size: 34px; line-height: 42px; }
  .contact__role,
  .contact__mobile { font-size: 22px; line-height: 33px; }
  .contact__address { margin-top: 26px; }
  .contact__line { font-size: 22px; line-height: 32.5px; }
  .skyline {
    position: absolute;
    left: 62px;
    top: 634px;
    width: 434px;
    height: 176px;
    background: linear-gradient(to top, var(--skyline-dark) 0%, var(--skyline-dark) 45%, var(--skyline-mid) 100%);
    opacity: 0.85;
  }
</style>
</head>
<body>
  <main class="card">
    <header class="brand-band">
      <span class="brand-name">NOVA PROPERTY MANAGERS</span>
    </header>

    <section class="contact">
      <p class="contact__name">Maren Holloway</p>
      <p class="contact__role">Director / Manager</p>
      <p class="contact__mobile">022 604 1958</p>
      <div class="contact__address">
        <p class="contact__line">Suite 4, 28 Quay Lane,</p>
        <p class="contact__line">Harbour Point, Westbay City</p>
        <p class="contact__line">Ph: (09) 471 2264</p>
        <p class="contact__line">Fax: (09) 471 2265</p>
        <p class="contact__line">Email: hello@novaliving.co.nz</p>
        <p class="contact__line">www.novaliving.co.nz</p>
      </div>
    </section>

    <div class="skyline" role="img" aria-label="Dark city skyline silhouette with a tall tower and a small grey sailboat on the water"></div>
  </main>
</body>
</html>
```